CrestQuote - Webstartup looking for some style

CrestQuote is a cloud based web application that allows construction sub-contractors to create and manage bids. Generally, these contractors will contact subcontractors to have them do specific parts of a larger construction project. This would be used by various subcontractors including woodwork (cabinetry), electricians, masons, etc...

Nearly all competitors are clients applications that have to be installed on the computer and are very expensive. This is a much lower cost alternative.

The business is just beginning and we want people to view us as a fresh alternative to companies that have been around for a long time and are starting to look a little dated.

We would like our logo included on the card (see attached). We have been using the circular 'cq' emblem seperately from the complete logo in various areas of the website. We lean towards a professional and clean look, with a tendancy more towards modern.

We want to differentiate ourselves from our competition which tend to be dated, complicated and less graphical.

(We are currently designing our public website as well - but don't have any designs yet)

Industry/Entity Type

Construction

Requirements
Must have
• Circular 'cq' emblem from logo. Probably entire logo, but not necessarily.

Should have reference to website: www.crestquote-example.com

The Url should be all lowercase (www.crestquote-example.com)
Should not have
• we do not want to list a phone number or email address on the cards. we want people to go to the actual website. we haven't decided if we want names printed on the business cards.

```html
<!DOCTYPE html>
<html lang="en">
<head>
<meta charset="utf-8">
<title>CrestQuote Business Cards</title>
<link rel="stylesheet" href="https://fonts.googleapis.com/css2?family=Lato:wght@400;700;900&display=swap">
<style>
  :root {
    --backdrop: #e4e4e4;
    --card: #f4f4f4;
    --card-edge: #e9e9e9;
    --panel: #fbfbfb;
    --ink: #1b1b1b;
    --icon: #4a4a4a;
    --brand-blue: #1f8fd0;
    --brand-orange: #f0a02a;
  }
  * { box-sizing: border-box; margin: 0; padding: 0; }
  html, body { width: 1200px; height: 900px; overflow: hidden; }
  body {
    background: var(--backdrop);
    font-family: "Lato", sans-serif;
    position: relative;
  }
  .card {
    position: absolute;
    width: 640px;
    height: 366px;
    border-radius: 26px;
    background: linear-gradient(160deg, var(--card), var(--card-edge));
    box-shadow: 0 10px 28px rgba(0,0,0,0.12);
  }
  .card-panel {
    position: absolute;
    background: var(--panel);
  }

  /* Back card: website */
  .card-back { left: 120px; top: 60px; }
  .card-back .card-panel { left: 76px; top: 40px; right: 28px; bottom: 40px; }
  .web-icon {
    position: absolute; left: 26px; top: 170px;
    width: 26px; height: 26px;
    stroke: var(--icon); fill: none; stroke-width: 1.6;
  }
  .contact-web {
    position: absolute; left: 106px; top: 166px;
    font-size: 25px; line-height: 34px; color: var(--ink);
  }
  .contact-web strong { font-weight: 900; }
  .side-brand {
    position: absolute; right: 44px; top: 54px; bottom: 54px; width: 40px;
    display: flex; flex-direction: column-reverse; align-items: center; gap: 12px;
  }
  .side-brand-dot { width: 34px; height: 34px; border-radius: 50%; background: var(--brand-blue); }
  .side-brand-name {
    writing-mode: vertical-rl; transform: rotate(180deg);
    font-size: 30px; font-weight: 400; color: var(--brand-blue);
  }

  /* Front card: emblem and name */
  .card-front { left: 440px; top: 470px; }
  .card-front .card-panel { left: 28px; top: 40px; right: 40px; bottom: 40px; }
  .emblem {
    position: absolute; left: 72px; top: 98px;
    display: flex; flex-direction: column; align-items: center; gap: 12px;
  }
  .emblem-circle { width: 136px; height: 136px; border-radius: 50%; background: var(--brand-orange); }
  .emblem-name { font-size: 20px; color: var(--brand-blue); }
  .holder { position: absolute; right: 96px; top: 148px; text-align: right; }
  .holder-name { font-size: 40px; font-weight: 900; color: var(--ink); line-height: 1; }
  .holder-role { font-size: 19px; color: var(--ink); margin-top: 4px; }
</style>
</head>
<body>
  <section class="card card-back">
    <div class="card-panel"></div>
    <svg class="web-icon" viewBox="0 0 26 26" aria-hidden="true"><rect x="7" y="4" width="12" height="19" rx="6" transform="rotate(-35 13 13)"/><path d="M10 9l4 6"/></svg>
    <p class="contact-web">www.<strong>crestquote-example</strong>.com</p>
    <div class="side-brand">
      <span class="side-brand-dot"></span>
      <span class="side-brand-name">CrestQuote</span>
    </div>
  </section>

  <section class="card card-front">
    <div class="card-panel"></div>
    <div class="emblem">
      <span class="emblem-circle"></span>
      <span class="emblem-name">CrestQuote</span>
    </div>
    <div class="holder">
      <p class="holder-name">Jonas Reed</p>
      <p class="holder-role">managing director</p>
    </div>
  </section>
</body>
</html>
```